Business Card Design for a coaching and consulting company (usage of existing logo)

We need a business card design for a new business start up (coaching & consulting) incorporating an existing logo that has just been created by a brandhollow designer.

The business card should pick up the existing logo and its colours (please check out variations as well) and look fresh, light, open and professional. The business card must be applicable for worldwide clients and must adhere to the standard Australian business card measurements. We are open for fun designs that require special print techniques as long as it doesn't get too expensive/fancy in the print process. We prefer versions that use both sides of the business card as we personally find 1-siders a little bit boring.

```html
<!DOCTYPE html>
<html lang="en">
<head>
<meta charset="utf-8">
<title>Beaconpoint Business Card</title>
<link rel="stylesheet" href="https://fonts.googleapis.com/css2?family=Exo+2:wght@400;500;600&display=swap">
<style>
  :root {
    --backdrop: #9a9c9b;
    --card: #f1f2f1;
    --ink: #4a4b4c;
    --ink-soft: #6b6c6d;
    --accent: #f7c64a;
    --slate: #626364;
    --rule: #7d7e7f;
  }
  * { box-sizing: border-box; margin: 0; padding: 0; }
  html, body {
    width: 1200px; height: 894px; overflow: hidden;
    background: var(--backdrop);
    font-family: "Exo 2", sans-serif;
    color: var(--ink);
  }
  .canvas { position: relative; width: 1200px; height: 894px; }
  .card {
    position: absolute; width: 540px; height: 330px;
    background: var(--card); overflow: hidden;
  }
  .card--front { left: 600px; top: 90px; }
  .card--details { left: 60px; top: 470px; }

  .brand { position: absolute; display: flex; flex-direction: column; }
  .brand__row { display: flex; align-items: center; gap: 10px; }
  .brand__dot { width: 14px; height: 14px; border-radius: 50%; background: var(--accent); }
  .brand__name { font-weight: 500; color: var(--ink-soft); letter-spacing: 0.5px; }
  .brand__tagline { color: var(--accent); font-weight: 400; }

  .card--front .brand { left: 48px; top: 54px; }
  .card--front .brand__name { font-size: 34px; }
  .card--front .brand__tagline { font-size: 15px; margin-left: 60px; margin-top: 2px; }

  .band {
    position: absolute; right: 0; height: 76px;
    border-radius: 38px 0 0 38px;
  }
  .band--accent { background: var(--accent); left: 330px; top: 178px; }
  .band--slate { background: var(--slate); left: 400px; top: 128px; height: 72px; border-radius: 36px 0 0 36px; }

  .person { position: absolute; left: 40px; top: 28px; }
  .person__name { font-size: 24px; font-weight: 400; letter-spacing: 0.5px; }
  .person__role { font-size: 10px; font-weight: 600; letter-spacing: 1px; text-transform: uppercase; margin-top: 2px; }
  .rule { position: absolute; height: 2px; background: var(--rule); }
  .rule--name { left: 40px; top: 80px; width: 310px; }
  .rule--contact { left: 40px; top: 208px; width: 500px; }
  .rule--base-1 { left: 40px; top: 274px; width: 500px; height: 1.5px; }
  .rule--base-2 { left: 70px; top: 296px; width: 470px; height: 1.5px; }

  .contact { position: absolute; left: 40px; top: 94px; display: grid; grid-template-columns: 82px auto; row-gap: 4px; font-size: 15px; }
  .contact dt { color: var(--ink-soft); }
  .contact dd { color: var(--ink); font-weight: 500; letter-spacing: 0.6px; }

  .address { position: absolute; left: 40px; top: 222px; display: flex; align-items: center; gap: 14px; font-size: 14px; letter-spacing: 0.8px; }

  .card--details .brand { right: 30px; bottom: 42px; align-items: flex-end; }
  .card--details .brand__name { font-size: 24px; }
  .card--details .brand__tagline { font-size: 11px; }
</style>
</head>
<body>
<main class="canvas">
  <section class="card card--front" aria-label="Card front">
    <div class="brand">
      <div class="brand__row"><span class="brand__dot"></span><span class="brand__name">Beaconpoint</span></div>
      <span class="brand__tagline">Coaching &amp; Consulting</span>
    </div>
    <div class="band band--accent"></div>
  </section>

  <section class="card card--details" aria-label="Card back">
    <div class="person">
      <p class="person__name">Daniel Harper</p>
      <p class="person__role">General Manager</p>
    </div>
    <div class="rule rule--name"></div>
    <dl class="contact">
      <dt>Phone:</dt><dd>012 555 0142</dd>
      <dt>Fax:</dt><dd>012 555 0143</dd>
      <dt>Email:</dt><dd>hello@beaconpoint.com</dd>
      <dt>website:</dt><dd>www.beaconpoint.com</dd>
    </dl>
    <div class="rule rule--contact"></div>
    <p class="address">
      <svg width="14" height="20" viewBox="0 0 14 20" aria-hidden="true"><path d="M7 0C3.1 0 0 3.1 0 7c0 5 7 13 7 13s7-8 7-13c0-3.9-3.1-7-7-7zm0 9.5A2.5 2.5 0 1 1 7 4.5a2.5 2.5 0 0 1 0 5z" fill="var(--ink)"/></svg>
      27, 9th floor, Harbour View Road NSW
    </p>
    <div class="band band--slate"></div>
    <div class="brand">
      <div class="brand__row"><span class="brand__dot"></span><span class="brand__name">Beaconpoint</span></div>
      <span class="brand__tagline">Coaching &amp; Consulting</span>
    </div>
    <div class="rule rule--base-1"></div>
    <div class="rule rule--base-2"></div>
  </section>
</main>
</body>
</html>
```